Business Card Design

An energy company designed around renewable energy and energy storage that focuses on providing its energy at points on the grid that reduce costs and add value to the system.

Industry/Entity Type

Business

Contact Information for Business Card

Martin Delacroix
Executive Vice President
41 K ST NE
Washington, DC 20017
240-555-0183
mdelacroix@harborvoltco.example

```html
<!DOCTYPE html>
<html lang="en">
<head>
<meta charset="utf-8">
<title>Harbor Voltco — Business Card</title>
<link rel="stylesheet" href="https://fonts.googleapis.com/css2?family=Arimo:wght@400;700&display=swap">
<style>
  :root {
    --page: #ffffff;
    --stage: #e6e7e8;
    --card: #000000;
    --green: #8dc63f;
    --muted: #8c8c84;
    --white: #ffffff;
    --grid-a: #9a9a88;
    --grid-b: #2a2a24;
  }
  * { margin: 0; padding: 0; box-sizing: border-box; }
  html, body {
    width: 1200px; height: 1179px; overflow: hidden;
    background: var(--page);
    font-family: "Arimo", Arial, sans-serif;
  }
  .stage {
    position: absolute; left: 4px; top: 4px;
    width: 1196px; height: 1175px;
    background: var(--stage);
    border-radius: 80px;
  }
  .card {
    position: absolute; left: 267px; top: 415px;
    width: 679px; height: 367px;
    background: var(--card);
  }
  .pattern {
    position: absolute; left: 22px; width: 263px;
    background: linear-gradient(180deg, var(--grid-b), var(--grid-a) 50%, var(--grid-b));
    opacity: 0.75;
  }
  .pattern--top { top: 40px; height: 66px; }
  .pattern--bottom { top: 244px; height: 82px; }
  .brand {
    position: absolute; left: 22px; top: 122px; width: 263px;
    text-align: center; color: var(--green); font-weight: 700;
    line-height: 1;
  }
  .brand__name { display: block; font-size: 56px; letter-spacing: 1px; }
  .brand__sub { display: block; font-size: 36px; margin-top: 4px; }
  .brand__web {
    position: absolute; left: 22px; top: 227px; width: 263px;
    text-align: center; color: var(--green);
    font-size: 11px; letter-spacing: 3px;
  }
  .person { position: absolute; left: 342px; top: 56px; }
  .person__name {
    color: var(--green); font-weight: 700;
    font-size: 25px; letter-spacing: 1.5px; text-transform: uppercase;
  }
  .person__title { color: var(--muted); font-size: 15px; margin-top: 9px; letter-spacing: 0.5px; }
  .contact { position: absolute; left: 342px; top: 221px; font-size: 18px; line-height: 22px; letter-spacing: 0.3px; }
  .contact__line { color: var(--white); }
  .contact__address { color: var(--green); margin-top: 16px; }
</style>
</head>
<body>
  <div class="stage">
    <div class="card">
      <div class="pattern pattern--top" role="img" aria-label="Decorative grid of fine lines"></div>
      <div class="brand">
        <span class="brand__name">HARBOR</span>
        <span class="brand__sub">voltco</span>
      </div>
      <div class="brand__web">www.harborvoltco.example</div>
      <div class="pattern pattern--bottom" role="img" aria-label="Decorative grid of fine lines"></div>

      <div class="person">
        <div class="person__name">Martin Delacroix</div>
        <div class="person__title">Executive Vice President</div>
      </div>

      <div class="contact">
        <div class="contact__line">240-555-0183</div>
        <div class="contact__line">mdelacroix@harborvoltco.example</div>
        <div class="contact__address">41 K ST NE Washington,<br>DC 20017</div>
      </div>
    </div>
  </div>
</body>
</html>
```